business card - Helicopter Flight Services, Flight School, etc.

We need a business card design for a new helicopter service.

We offer Helicopter Flight Services, Aerial Filming & Photography, Flight School, and Helicopter Tours. In that order.

Summit BladeLine, Inc.
Harold Tebbets
SummitBladeline@Mailvane.com
555-014-2786

Based at the Corvell Airport in Van Nuys, CA. The final design should communicate integrity and safety. Pictures or logos at your discretion.

Card back side - surprise me.

```html
<!DOCTYPE html>
<html lang="en">
<head>
<meta charset="utf-8">
<title>Summit BladeLine, Inc. — Business Card</title>
<link rel="stylesheet" href="https://fonts.googleapis.com/css2?family=Montserrat:wght@700&family=Open+Sans:wght@400;700&display=swap">
<style>
  :root {
    --backdrop: #e9e7e3;
    --card-white: #ffffff;
    --card-black: #0b0b0c;
    --blue: #2d95d8;
    --blue-light: #5bb8ec;
    --blue-deep: #1c6fb3;
    --text-light: #f2f2f2;
  }
  * { margin: 0; padding: 0; box-sizing: border-box; }
  html, body { width: 1200px; height: 913px; overflow: hidden; }
  body {
    background: var(--backdrop);
    font-family: "Open Sans", Arial, sans-serif;
    position: relative;
  }
  .card {
    position: absolute;
    width: 525px;
    height: 300px;
    border-radius: 16px;
    overflow: hidden;
    box-shadow: 0 14px 30px rgba(0,0,0,0.25);
  }
  .card-front { left: 45px; top: 160px; background: var(--card-white); }
  .card-back  { left: 630px; top: 453px; background: var(--card-black); }
  .front-wave { position: absolute; inset: 0; width: 100%; height: 100%; }

  .brand {
    position: absolute;
    display: flex;
    align-items: center;
    gap: 10px;
    font-family: "Montserrat", Arial, sans-serif;
    font-weight: 700;
    color: var(--blue);
    letter-spacing: 0.5px;
    white-space: nowrap;
    z-index: 1;
  }
  .brand-dot {
    width: 26px; height: 26px;
    border-radius: 50%;
    background: var(--blue);
    flex: none;
  }
  .card-front .brand { right: 34px; top: 52px; font-size: 22px; }

  .contact {
    position: absolute;
    left: 30px;
    bottom: 26px;
    color: var(--text-light);
    z-index: 1;
  }
  .contact-name { font-weight: 700; font-size: 21px; line-height: 1.2; }
  .contact-role { color: var(--blue); font-size: 14px; margin-bottom: 8px; }
  .contact-line {
    display: flex; align-items: center; gap: 8px;
    font-size: 14px; line-height: 1.5;
  }
  .contact-line svg { width: 14px; height: 14px; flex: none; }

  .card-back .brand {
    left: 50%; top: 92px; transform: translateX(-50%);
    font-size: 22px;
  }
  .services {
    position: absolute;
    left: 0; right: 0; top: 160px;
    text-align: center;
    color: var(--text-light);
    font-size: 15px;
    line-height: 1.45;
    list-style: none;
  }
</style>
</head>
<body>

  <section class="card card-front" aria-label="Business card front">
    <svg class="front-wave" viewBox="0 0 525 300" preserveAspectRatio="none" aria-hidden="true">
      <path d="M0,140 C150,115 300,200 525,100 L525,300 L0,300 Z" fill="var(--blue-light)"/>
      <path d="M0,150 C150,125 300,210 525,110 L525,300 L0,300 Z" fill="var(--blue)"/>
      <path d="M0,162 C150,137 300,222 525,122 L525,300 L0,300 Z" fill="var(--card-black)"/>
    </svg>

    <div class="brand"><span class="brand-dot"></span>SUMMIT BLADELINE, INC.</div>

    <div class="contact">
      <p class="contact-name">Harold Tebbets</p>
      <p class="contact-role">Owner</p>
      <p class="contact-line">
        <svg viewBox="0 0 16 16" aria-hidden="true"><path fill="var(--blue)" d="M3.6 1.2l2.3 2.7-1.3 1.7c.9 2 2.5 3.6 4.5 4.5l1.7-1.3 2.7 2.3-1.4 2.3C7 12.9 3.1 9 2.1 3.1z"/></svg>
        555-014-2786
      </p>
      <p class="contact-line">
        <svg viewBox="0 0 16 16" aria-hidden="true"><rect x="1.5" y="3.5" width="13" height="9" rx="1" fill="none" stroke="var(--blue)" stroke-width="1.5"/><path d="M2 4.2l6 4.6 6-4.6" fill="none" stroke="var(--blue)" stroke-width="1.5"/></svg>
        SummitBladeline@Mailvane.com
      </p>
    </div>
  </section>

  <section class="card card-back" aria-label="Business card back">
    <div class="brand"><span class="brand-dot"></span>SUMMIT BLADELINE</div>
    <ul class="services">
      <li>Aerial Filming &amp; Photography</li>
      <li>Flight School</li>
      <li>Helicopter Tours (In that order)</li>
    </ul>
  </section>

</body>
</html>
```